Elegant, High End Integrated Wellness Healthcare Practice

We need a brochure designed for an integrated mind-body wellness healthcare practice (www.larchveilclinic.com) . This brochure will be used when we cold call prospects (physicians to refer to our office, and potential consumers to utilize our services). Our practice is geographically located in the middle Tennessee USA region, although we have plans to become an international company as many of our offerings can be accessed anywhere in the world. Ultimately our goal is to have this brochure used as a leave-behind in an effort to introduce our integrated offerings to increase market share. The final product brochure should be both elegant and serious, with clean lines but also convey warmth and trust, as individuals who are coming for our services have usually struggled with their health for a significant amount of time before finding our practice.

The design brief was very specific about providing a high-end science-based 2-page brochure (not flier). Several designs submitted were fliers. The other designs were heavy on yoga or "woo woo" non-science-based looking pictures. This is a flier to appeal to physicians and other healthcare providers. Therefore the design must speak science and evidence-based methods of mind and body wellness care. I would also like to appeal to the other designers I paid extra for their submissions and who have indicated they will "respond in the coming days."

```html
<!DOCTYPE html>
<html lang="en">
<head>
<meta charset="utf-8">
<title>Larchveil Clinic – Flyer</title>
<link rel="stylesheet" href="https://fonts.googleapis.com/css2?family=Red+Hat+Display:ital,wght@0,400;0,500;0,700;0,800;1,500&display=swap">
<style>
  :root {
    --page-bg: #7d9869;
    --leaf: #5d9c3a;
    --leaf-light: #76b446;
    --leaf-deep: #3e7a26;
    --forest: #24341b;
    --white: #ffffff;
    --cream: #f3f1ea;
    --accent: #e8662c;
    --photo-dark: #4a3a2c;
    --photo-mid: #8a6a48;
    --photo-light: #c9a57a;
  }
  * { box-sizing: border-box; margin: 0; padding: 0; }
  html, body { width: 1200px; height: 1200px; overflow: hidden; }
  body {
    background: var(--page-bg);
    font-family: "Red Hat Display", Arial, sans-serif;
    position: relative;
  }
  .flyer {
    position: absolute;
    left: 220px; top: 62px;
    width: 760px; height: 1075px;
    overflow: hidden;
    background: var(--forest);
    box-shadow: 0 10px 30px rgba(0,0,0,.25);
  }
  .flyer-shapes { position: absolute; inset: 0; }
  .brand {
    position: absolute; left: 0; top: 50px;
    width: 274px; height: 62px;
    background: var(--white);
    border-radius: 0 31px 31px 0;
    display: flex; align-items: center; gap: 12px;
    padding-left: 40px;
  }
  .brand-dot {
    width: 40px; height: 40px; border-radius: 50%;
    background: var(--leaf-deep); flex: none;
  }
  .brand-name {
    font-size: 19px; font-weight: 500; line-height: 1.15;
    color: var(--forest); letter-spacing: .5px;
    text-transform: uppercase;
  }
  .headline {
    position: absolute; right: 42px; top: 368px;
    text-align: right; color: var(--white);
    font-weight: 800; font-size: 51px; line-height: 52px;
    letter-spacing: .3px;
  }
  .services {
    position: absolute; top: 604px;
    list-style: none; color: var(--white);
    font-size: 19px; line-height: 28px; font-weight: 400;
  }
  .services.col-a { left: 40px; }
  .services.col-b { left: 351px; }
  .services li::before { content: "> "; }
  .services .more { font-style: italic; font-weight: 700; }
  .services .more::before { content: ""; }
  .contact {
    position: absolute; right: 40px; top: 897px;
    text-align: right; color: var(--white);
    font-size: 19px; line-height: 25px;
  }
  .contact p { display: flex; align-items: center; justify-content: flex-end; gap: 10px; }
  .contact .address { margin-top: 13px; }
  .contact .web {
    margin-top: 23px; color: var(--accent);
    font-style: italic; font-weight: 500; letter-spacing: 3.5px; font-size: 20px;
  }
  .icon { width: 13px; height: 13px; flex: none; }
</style>
</head>
<body>
  <main class="flyer">
    <svg class="flyer-shapes" viewBox="0 0 760 1075" width="760" height="1075" aria-hidden="false">
      <defs>
        <linearGradient id="photoTone" x1="0" y1="0" x2="1" y2="1">
          <stop offset="0" stop-color="var(--photo-dark)"/>
          <stop offset=".55" stop-color="var(--photo-mid)"/>
          <stop offset="1" stop-color="var(--photo-light)"/>
        </linearGradient>
        <linearGradient id="leafBand" x1="0" y1="0" x2="0" y2="1">
          <stop offset="0" stop-color="var(--leaf-light)"/>
          <stop offset=".6" stop-color="var(--leaf)"/>
          <stop offset="1" stop-color="var(--leaf-deep)"/>
        </linearGradient>
      </defs>
      <rect class="hero-photo" x="0" y="0" width="760" height="560" fill="url(#photoTone)" role="img" aria-label="Photo of herbal remedies: honey jars, ginger root, a white ceramic jug with a frangipani flower and a mortar on a wooden table"/>
      <path class="band-green" d="M760,150 C700,330 500,350 250,372 C80,388 0,430 0,470 L0,1075 L760,1075 Z" fill="url(#leafBand)"/>
      <path class="edge-line" d="M760,150 C700,330 500,350 250,372 C80,388 0,430 0,470" fill="none" stroke="var(--white)" stroke-width="6"/>
      <path class="swoosh" d="M0,470 C40,560 300,555 420,560 C560,566 650,600 690,642" fill="none" stroke="var(--white)" stroke-width="2.5"/>
      <path class="band-forest" d="M0,1075 L0,960 C150,850 450,850 760,795 L760,1075 Z" fill="var(--forest)"/>
      <path class="edge-line" d="M0,962 C150,852 450,852 760,797" fill="none" stroke="var(--white)" stroke-width="5"/>
      <path class="footer-rule" d="M0,1037 L295,1037" stroke="var(--white)" stroke-width="2.5"/>
    </svg>

    <div class="brand">
      <span class="brand-dot"></span>
      <span class="brand-name">Larchveil<br>Clinic</span>
    </div>

    <h1 class="headline">DISCOVER<br>A BETTER WAY<br>TO A BETTER YOU</h1>

    <ul class="services col-a">
      <li>Sonal Brain Care</li>
      <li>Functional Medicine</li>
      <li>Healthy Lifestyle Package</li>
      <li>Lumivra for Pain</li>
      <li>Wellness Package</li>
      <li>Mind Health</li>
      <li>Body Health</li>
      <li>Sleep Restoration</li>
    </ul>
    <ul class="services col-b">
      <li>Whole Body Wellness</li>
      <li>Nutrional Wellness</li>
      <li>360° Integrative Wellness</li>
      <li>Brain Wave Mapping</li>
      <li>ADHD</li>
      <li>Stress Management</li>
      <li>Corelens Scan</li>
      <li class="more">more...</li>
    </ul>

    <div class="contact">
      <p>New Patients: (615) 555-0142
        <svg class="icon" viewBox="0 0 16 16"><path d="M3 1l3 3-1.5 2a9 9 0 0 0 5.5 5.5L12 10l3 3-2 2C7 15 1 9 1 3z" fill="var(--accent)"/></svg></p>
      <p>Existing Patients: (615) 555-0187
        <svg class="icon" viewBox="0 0 16 16"><path d="M3 1l3 3-1.5 2a9 9 0 0 0 5.5 5.5L12 10l3 3-2 2C7 15 1 9 1 3z" fill="var(--accent)"/></svg></p>
      <p class="address">4180 Alder Crest Dr, Murfreesboro, TN 37128, United States
        <svg class="icon" viewBox="0 0 16 16"><path d="M8 0a5 5 0 0 0-5 5c0 4 5 11 5 11s5-7 5-11a5 5 0 0 0-5-5zm0 7a2 2 0 1 1 0-4 2 2 0 0 1 0 4z" fill="var(--accent)"/></svg></p>
      <p class="web">www.larchveilclinic.com
        <svg class="icon" viewBox="0 0 16 16"><circle cx="8" cy="8" r="7" fill="none" stroke="var(--cream)" stroke-width="1.5"/><path d="M1 8h14M8 1c-3 4-3 10 0 14M8 1c3 4 3 10 0 14" fill="none" stroke="var(--cream)" stroke-width="1.2"/></svg></p>
    </div>
  </main>
</body>
</html>
```